Zielgruppe
Wir betreiben eine Bäckerei mit Kaffeehaus als Nahversorger in A-3032 Eichgraben. Das design soll natürlich unsere Kunden ansprechen.
Aufgabenstellung
Es wird ein neuer Schriftzug horizontal für das Sanierungsobjekt gesucht. Folgende Vorgaben sind wünschenswert:
Schriftzug - Außenbeschilderung;
Schriftzug -Cafe- linksbündig, Schriftzug -Kleffinger- mittig, Schriftzug -Bäckerei- rechstbündig. Die Außenbeschilderung soll ca. 5m lang und ca. 70cm hoch sein. Siehe auch Bestandsobjekt im Anhang. Vorraussetzung ist, das das Design auf ALU oder Plexiglas folierbar ist.
Familienwappen;
Eine Druckversion ist im Anhang ersichtlich, eine vereinfachte Darstellung wäre durchaus möglich durch etwa Konturen/ Linien etc..
Farben;
Am Foto ersichtlich die neue Farbe der Fassade links und rechts.
Banner für zwischen den Fenstern - vertikal;
1x Design für Bäckerei (Semmel/ Brötchen, Korb mit Gebäck, etc.), Schriftzug oben -Bäckerei-, Schriftzug unten -Kleffinger-.
1x Design für Cafe (Kaffeetasse, Cupcake, etc), Schriftzug oben -Cafe-, Schriftzug unten -Kleffinger-.
Designvorschlag; helle Schrift auf dunklem Hintergrund- weinrot, smaragtgrün, dunkelblau???
Natürlich sind auch alternative/ abweichende Vorschläge wünschenswert.
Wir freuen uns auf die Designs !!!

```html
<!DOCTYPE html>
<html lang="de">
<head>
<meta charset="utf-8">
<title>Kleffinger – Cafe &amp; Bäckerei Beschilderung</title>
<link rel="stylesheet" href="https://fonts.googleapis.com/css2?family=Cinzel:wght@400&family=Kaushan+Script&family=Open+Sans:wght@400;600&display=swap">
<style>
  :root {
    --wine: #be1e2d;
    --wine-tint: #f2d2d5;
    --paper: #ffffff;
  }
  html, body {
    margin: 0;
    padding: 0;
    width: 1200px;
    height: 1200px;
    overflow: hidden;
    background: var(--paper);
  }
  .canvas {
    position: relative;
    width: 1200px;
    height: 1200px;
  }
  .facade-sign {
    position: absolute;
    left: 92px;
    top: 348px;
    width: 1016px;
    height: 82px;
    background: var(--wine);
    border-radius: 32px;
    box-sizing: border-box;
  }
  .facade-sign::after {
    content: "";
    position: absolute;
    inset: 7px;
    border: 2px solid var(--paper);
    border-radius: 26px;
  }
  .script {
    font-family: "Kaushan Script", cursive;
    font-weight: 400;
    position: absolute;
    line-height: 1;
    white-space: nowrap;
    margin: 0;
  }
  .facade-sign .script { color: var(--paper); }
  .facade-sign .word-cafe { left: 158px; top: 8px; font-size: 56px; }
  .facade-sign .word-baeckerei { left: 680px; top: 14px; font-size: 49px; }
  .facade-sign .brand {
    position: absolute;
    left: 0;
    width: 932px;
    top: 14px;
    text-align: center;
    font-family: "Cinzel", serif;
    font-size: 50px;
    color: var(--paper);
    line-height: 1;
    letter-spacing: 1px;
  }
  .banner {
    position: absolute;
    top: 444px;
    width: 256px;
    height: 558px;
    border: 9px solid var(--wine);
    box-sizing: border-box;
  }
  .banner::before {
    content: "";
    position: absolute;
    inset: 5px;
    border: 2px solid var(--wine);
  }
  .banner-bakery { left: 329px; }
  .banner-cafe { left: 615px; }
  .banner .script {
    left: 0;
    right: 0;
    text-align: center;
    color: var(--wine);
  }
  .banner-bakery .banner-title { top: 24px; font-size: 51px; }
  .banner-cafe .banner-title { top: 12px; font-size: 72px; }
  .banner-art {
    position: absolute;
    background: var(--wine-tint);
    border-radius: 10px;
  }
  .banner-bakery .banner-art { left: 14px; top: 174px; width: 211px; height: 104px; }
  .banner-cafe .banner-art { left: 45px; top: 137px; width: 146px; height: 149px; }
  .banner-brand {
    position: absolute;
    left: 0;
    right: 0;
    top: 338px;
    text-align: center;
    font-family: "Cinzel", serif;
    font-size: 22px;
    color: var(--wine);
    line-height: 1;
  }
  .banner-tagline {
    position: absolute;
    left: 0;
    right: 6px;
    top: 362px;
    text-align: center;
    font-family: "Open Sans", sans-serif;
    font-size: 11px;
    line-height: 14px;
    color: var(--wine);
    margin: 0;
  }
  .crest {
    position: absolute;
    left: 77px;
    top: 398px;
    width: 83px;
    height: 96px;
    background: var(--wine-tint);
    border-radius: 8px 8px 40px 40px;
  }
  .crest-caption {
    position: absolute;
    left: 0;
    right: 6px;
    top: 501px;
    text-align: center;
    font-family: "Open Sans", sans-serif;
    font-weight: 600;
    font-size: 7px;
    color: var(--wine);
    margin: 0;
  }
</style>
</head>
<body>
<main class="canvas">
  <div class="facade-sign">
    <span class="script word-cafe">Cafe</span>
    <span class="brand">KLEFFINGER</span>
    <span class="script word-baeckerei">Bäckerei</span>
  </div>

  <section class="banner banner-bakery">
    <h2 class="script banner-title">Bäckerei</h2>
    <div class="banner-art" role="img" aria-label="Brotlaib im Kreis, eingerahmt von Weizenähren"></div>
    <div class="banner-brand">KLEFFINGER</div>
    <p class="banner-tagline">DIE BÄCKEREI IN<br>EICHRABEN</p>
    <div class="crest" role="img" aria-label="Familienwappen"></div>
    <p class="crest-caption">FAMILIENWAPPEN SEIT 1380</p>
  </section>

  <section class="banner banner-cafe">
    <h2 class="script banner-title">Cafe</h2>
    <div class="banner-art" role="img" aria-label="Dampfende Kaffeetasse auf Untertasse mit Kaffeebohnen"></div>
    <div class="banner-brand">KLEFFINGER</div>
    <p class="banner-tagline">DIE BÄCKEREI IN<br>EICHRABEN</p>
    <div class="crest" role="img" aria-label="Familienwappen"></div>
    <p class="crest-caption">FAMILIENWAPPEN SEIT 1380</p>
  </section>
</main>
</body>
</html>
```